2018 Mother's Day and Baby Blessing poster

I need a poster Mother's Day and Baby Blessing ceremony for a Jade Petal Celebration at Sydney Kestrel Cove. There is no specification on the design, however the only requirement is to present mother and baby in the poster. I would like the design to be modern, attractive and simple.

Must have:
Date: 13/5/2018 (Sunday)
Time: 2:00pm (1:00pm registration)
Venue: Wirraminta Park, Kestrel Cove
Logo

```html
<!DOCTYPE html>
<html lang="en">
<head>
<meta charset="utf-8">
<title>Mother's Day and Baby Blessing</title>
<link rel="stylesheet" href="https://fonts.googleapis.com/css2?family=Open+Sans:wght@700;800&family=Cutive+Mono&display=swap">
<style>
  :root {
    --plum: #3d0044;
    --ink-light: #ebe4ee;
    --text-white: #ffffff;
    --accent-yellow: #f2d84a;
    --art-magenta: #a61fb4;
    --art-magenta-deep: #7c168f;
  }
  html, body {
    margin: 0;
    padding: 0;
    overflow: hidden;
    background: var(--plum);
  }
  .poster {
    position: relative;
    width: 776px;
    height: 1200px;
    background: var(--plum);
    overflow: hidden;
  }
  .mother-baby-art {
    position: absolute;
    left: 318px;
    top: 190px;
    width: 448px;
    height: 755px;
    border-radius: 40px 20px 160px 60px / 40px 30px 260px 120px;
    background: linear-gradient(160deg, var(--art-magenta), var(--art-magenta-deep));
    opacity: 0.85;
  }
  .headline {
    position: absolute;
    left: 0;
    margin: 0;
    font-family: "Open Sans", sans-serif;
    font-weight: 700;
    line-height: 1;
    color: var(--ink-light);
    white-space: nowrap;
  }
  .headline--large { font-size: 144px; letter-spacing: -3px; left: 30px; }
  .headline--medium { font-size: 54px; letter-spacing: 0; left: 32px; }
  .headline--mothers { top: 12px; }
  .headline--dayand { top: 172px; }
  .headline--baby { top: 230px; font-size: 130px; letter-spacing: -2px; left: 34px; }
  .headline--blessing { top: 378px; }

  .detail {
    position: absolute;
    left: 29px;
    margin: 0;
    font-family: "Cutive Mono", monospace;
    line-height: 1;
    color: var(--text-white);
    white-space: nowrap;
  }
  .detail-label { font-size: 34px; }
  .detail-value { font-size: 60px; }
  .venue-label { top: 548px; }
  .venue-line1 { top: 592px; }
  .venue-line2 { top: 650px; }
  .date-label { top: 800px; }
  .date-value { top: 840px; font-size: 62px; }
  .date-day { top: 892px; font-size: 62px; letter-spacing: 4px; color: var(--accent-yellow); }
  .time-label { top: 1055px; }
  .time-value { top: 1092px; font-size: 66px; }
  .time-note { top: 1157px; font-size: 21px; color: var(--accent-yellow); }

  .festival-name {
    position: absolute;
    right: 24px;
    top: 1090px;
    width: 300px;
    margin: 0;
    font-family: "Open Sans", sans-serif;
    font-weight: 700;
    font-size: 30px;
    line-height: 1.1;
    color: var(--text-white);
    text-align: right;
  }
</style>
</head>
<body>
  <main class="poster">
    <div class="mother-baby-art" role="img" aria-label="Halftone dotted silhouette of a mother holding her baby"></div>

    <h1 class="headline headline--large headline--mothers">MOTHER’S</h1>
    <p class="headline headline--medium headline--dayand">DAY AND</p>
    <p class="headline headline--baby">BABY</p>
    <p class="headline headline--medium headline--blessing">BLESSING</p>

    <p class="detail detail-label venue-label">Venue:</p>
    <p class="detail detail-value venue-line1">Wirraminta Park,</p>
    <p class="detail detail-value venue-line2">Kestrel Cove</p>

    <p class="detail detail-label date-label">Date:</p>
    <p class="detail date-value">13/5/2018</p>
    <p class="detail date-day">SUNDAY</p>

    <p class="detail detail-label time-label">Time:</p>
    <p class="detail time-value">2:00pm</p>
    <p class="detail time-note">(registration 1:00 pm)</p>

    <p class="festival-name">Jade Petal Celebration</p>
  </main>
</body>
</html>
```